Design a Poster to Advertise Pip'n'Tumble at the Netball Stadium

Objective:
Create an eye-catching and enticing poster to promote Pip'n'Tumble, a ready-to-eat snack, at a netball stadium where large numbers of players, families, and friends gather weekly. The goal is to attract attention, stimulate appetite, and encourage purchases from both kids and adults.
Key Elements to Include:
Company Logo:
Incorporate our logo prominently to ensure brand recognition.
Product Description:
Feature a mouth-watering description: "Deliciously cheesy, oozy mac'n'cheese hand-rolled into bite-sized balls and coated in a crispy, crunchy panko crumb." This should be paired with an enticing image of the product.
Serving Suggestion:
Include a high-quality image showing Pip'n'Tumble balls served in an appealing way. The visual should highlight the crispy exterior and gooey interior to emphasize the product's deliciousness.
Catchy Tagline or Slogan:
Develop a fun and engaging tagline that appeals to kids and encourages them to persuade their parents to buy the product. For example, “Grab a Cheesy Treat Today!” or “The Snack Everyone's Cheering For!”
Visual Appeal:
Use vibrant colors and dynamic design elements to draw attention. The poster should create a visual feast that makes Pip'n'Tumble irresistible.
Include essential details such as:
The location where Pip'n'Tumble will be available at the stadium.
Pricing information if relevant.
Promote that is locally South Australian made with all natural ingredients
Call to Action:
Add a compelling call to action that encourages immediate purchase, such as “Get Yours Now!” or “Don’t Miss Out!”
Layout:
Ensure the design is clean and organized, with a clear hierarchy of information. The poster should be easy to read from a distance.
Design Specifications:
Size: A3 or larger
Notes:
The poster should appeal to both children and adults, emphasizing the irresistible taste and texture of Pip'n'Tumble. The design should make the product a must-have snack at the netball stadium.
Target Market(s)
10 year olds to 18 year olds
Industry/Entity Type
food
Look and feel

```html
<!DOCTYPE html>
<html lang="en">
<head>
<meta charset="utf-8">
<title>Pip'n'Tumble – Stadium Poster</title>
<link rel="stylesheet" href="https://fonts.googleapis.com/css2?family=Anton&family=Bebas+Neue&family=Barlow+Condensed:wght@500;600&family=Montserrat:wght@600&family=Kalam:wght@700&display=swap">
<style>
  :root {
    --canvas-bg: #e6e6e4;
    --night: #15161a;
    --white: #ffffff;
    --brand-orange: #ec6a1f;
    --band-red: #a8363a;
    --band-gold: #e8a440;
    --ink: #1c1c1c;
  }
  * { box-sizing: border-box; margin: 0; padding: 0; }
  html, body { width: 1200px; height: 874px; overflow: hidden; background: var(--canvas-bg); }

  .poster {
    position: absolute; left: 291px; top: 0;
    width: 618px; height: 874px; overflow: hidden;
    background: var(--night);
  }
  .stadium-photo {
    position: absolute; inset: 0;
    background:
      radial-gradient(ellipse 240px 160px at 140px 270px, rgba(255,236,200,.9), rgba(242,201,138,.5) 45%, rgba(242,201,138,0) 80%),
      linear-gradient(180deg, #111216 0%, #2b2a2c 18%, #6d5d4d 33%, #8a7560 42%, #3c3735 55%, #1f2320 70%, #2e3b22 85%, #23301c 100%);
  }
  .artwork { position: absolute; inset: 0; width: 618px; height: 874px; }

  .brand {
    position: absolute; left: 44px; top: 186px;
    display: flex; align-items: center; gap: 10px;
    font-family: "Barlow Condensed", sans-serif; font-weight: 600;
    font-size: 32px; line-height: 1; color: var(--white);
  }
  .brand-dot { width: 16px; height: 16px; border-radius: 50%; background: var(--white); }

  .product-name {
    position: absolute; left: 252px; top: 80px;
    font-family: "Anton", sans-serif; font-weight: 400; font-size: 62px; line-height: 1;
    color: var(--white); letter-spacing: .5px; white-space: nowrap;
    -webkit-text-stroke: 4px var(--brand-orange); paint-order: stroke fill;
    transform: rotate(-9deg); transform-origin: left bottom;
  }
  .product-description {
    position: absolute; left: 285px; top: 124px; width: 292px;
    font-family: "Montserrat", sans-serif; font-weight: 600;
    font-size: 14.5px; line-height: 1.35; text-align: center; color: var(--white);
    transform: rotate(-7deg);
  }

  .tagline {
    position: absolute; left: 43px; top: 340px;
    font-family: "Bebas Neue", sans-serif; font-weight: 400; color: var(--white); line-height: 1;
    text-shadow: 0 2px 8px rgba(0,0,0,.35);
  }
  .tagline-lead { display: block; font-size: 47px; letter-spacing: .6px; }
  .tagline-main { display: block; font-size: 92px; letter-spacing: 2.4px; margin-top: -4px; }

  .cta-badge {
    position: absolute; left: 40px; top: 493px;
    width: 194px; height: 194px; border-radius: 50%;
    background: var(--white);
    display: flex; flex-direction: column; align-items: center; justify-content: center;
    font-family: "Kalam", cursive; font-weight: 700; color: var(--brand-orange);
    font-size: 44px; line-height: .85; transform: rotate(-10deg);
  }

  .location-note {
    position: absolute; left: 21px; top: 760px; width: 220px;
    font-family: "Barlow Condensed", sans-serif; font-weight: 500;
    font-size: 27px; line-height: 1.07; color: var(--white);
  }
  .origin-note {
    position: absolute; right: 23px; top: 764px; width: 230px;
    font-family: "Barlow Condensed", sans-serif; font-weight: 500;
    font-size: 22px; line-height: 1.06; text-align: right; color: var(--ink);
  }
</style>
</head>
<body>
  <main class="poster">
    <div class="stadium-photo" role="img" aria-label="Photo of a floodlit sports stadium under a sunset sky"></div>

    <svg class="artwork" viewBox="0 0 618 874">
      <defs>
        <radialGradient id="snack-tones" cx="0.58" cy="0.45" r="0.62">
          <stop offset="0" stop-color="#f3d9a2"/>
          <stop offset="0.3" stop-color="#e8a15a" stop-opacity="0.97"/>
          <stop offset="0.7" stop-color="#c9652a" stop-opacity="0.9"/>
          <stop offset="1" stop-color="#8f4220" stop-opacity="0"/>
        </radialGradient>
      </defs>
      <rect role="img" aria-label="Photo of crumbed mac and cheese balls in a bowl, one broken open to show the cheesy centre"
        x="110" y="400" width="540" height="370" fill="url(#snack-tones)"/>
      <path class="band-red" fill="var(--band-red)"
        d="M0 642 L40 668 L70 680 L95 700 L140 712 L200 718 L250 726 L300 728 L350 722 L410 718 L470 712 L520 705 L570 700 L618 694 L618 874 L0 874 Z"/>
      <path class="band-gold" fill="var(--band-gold)"
        d="M286 742 L320 746 L340 738 L380 742 L420 728 L455 732 L490 712 L520 716 L560 690 L590 686 L618 664 L618 874 L262 874 L300 830 L270 818 L330 796 L290 784 L340 770 L300 758 Z"/>
    </svg>

    <div class="brand"><span class="brand-dot"></span>Lumo Kitchen</div>

    <h1 class="product-name">PIP'N'TUMBLE</h1>
    <p class="product-description">Deliciously cheesy, oozy<br>mac'n'cheese hand-rolled into<br>bite-sized balls and coated in a<br>crispy, crunchy panko crumb.</p>

    <h2 class="tagline">
      <span class="tagline-lead">THE SNACK EVERYONE'S</span>
      <span class="tagline-main">CHEERING FOR!</span>
    </h2>

    <div class="cta-badge"><span>don't</span><span>miss</span><span>out!</span></div>

    <p class="location-note">Pip'n'Tumble will<br>be available at<br>the stadium.</p>
    <p class="origin-note">locally South Australian<br>made with all natural<br>ingredients</p>
  </main>
</body>
</html>
```